Flyer for the Radiant Harvest Worship Day 2020

I am looking to create a flyer for a one day prayer retreat our church is organizing.
This flyer will be posted on social media, websites and will also be printed so it can be mailed to people.
I am looking for something professional, with good use of our logo and band colors (logo colors).
I am counting on the designer's skill, creativity, art and knowledge of media communication to produce a flyer that will effectively and quickly convey the message we are trying to spread.
CONTENT OF THE FLYER:
Event title: Radiant Harvest Worship Day
Date: Tuesday July 2nd, 2020
Time: 11:00AM - 7:00PM
Belmora Hotel, 4876 Willowmere Street, Portland, Maine 04987 (Room: Evergrove)
Event Key words to highlight what the event is about: Prayer, Sharing the Word, Panel discussion, prophecy, Impartation.
Key phrases:
A one day prayer retreat.
Jesus Chris is Lord
Contact info:
www.toluvek.org
Phone: 207 555 0183
Email: contact@brightmeadowfold.org

```html
<!DOCTYPE html>
<html lang="en">
<head>
<meta charset="utf-8">
<title>Radiant Harvest Worship Day 2020</title>
<link rel="stylesheet" href="https://fonts.googleapis.com/css2?family=Cinzel:wght@700&family=Cardo:wght@400;700&family=Dancing+Script:wght@600&family=Michroma&family=Alegreya+Sans:wght@500&display=swap">
<style>
  :root {
    --navy: #013a5f;
    --teal: #026470;
    --teal-deep: #015863;
    --orange: #f39420;
    --gold: #ecc94f;
    --red: #f2333a;
    --ink: #2c4257;
    --keyword: #0b6872;
    --line: #6fc4b3;
    --white: #ffffff;
  }
  * { margin: 0; padding: 0; box-sizing: border-box; }
  html, body { width: 846px; height: 1200px; overflow: hidden; background: #fff; }
  .flyer { position: relative; width: 846px; height: 1200px; overflow: hidden; }
  .photo {
    position: absolute; inset: 0;
    background:
      radial-gradient(ellipse 260px 360px at 520px 860px, #3e4a4c 0%, #56605c 55%, rgba(86,96,92,0) 100%),
      linear-gradient(180deg, #f8efe0 0%, #f3e7cf 35%, #e3dbb4 55%, #b7b792 72%, #7d8a7a 100%);
  }
  .shapes { position: absolute; inset: 0; }
  .brand {
    position: absolute; top: 96px; right: 42px;
    font-family: "Cardo", serif; font-weight: 400; font-size: 56px;
    color: var(--white); letter-spacing: 2px; line-height: 1;
  }
  .contacts { position: absolute; top: 200px; right: 10px; list-style: none; }
  .contacts li {
    display: flex; align-items: center; justify-content: flex-end; gap: 8px;
    height: 39px;
    font-family: "Alegreya Sans", sans-serif; font-weight: 500; font-size: 19px; color: var(--white);
  }
  .contacts .icon {
    width: 29px; height: 29px; border-radius: 50%; background: var(--gold);
    display: flex; align-items: center; justify-content: center;
  }
  .title {
    position: absolute; top: 392px; left: 0; width: 846px; text-align: center;
    font-family: "Cinzel", serif; font-weight: 700; color: var(--ink);
    font-size: 66px; line-height: 88px; letter-spacing: 1px;
    text-shadow: 0 0 2px #fff, 0 0 2px #fff, 1px 1px 0 #fff, -1px -1px 0 #fff, 2px 3px 4px rgba(0,0,0,0.25);
  }
  .title .cap { font-size: 94px; }
  .tagline {
    position: absolute; top: 578px; left: 0; width: 846px; text-align: center;
    font-family: "Dancing Script", cursive; font-weight: 600; font-size: 29px; color: #3b3a35;
  }
  .keywords {
    position: absolute; top: 716px; left: 30px;
    font-family: "Michroma", sans-serif; font-size: 20px; line-height: 32px; color: var(--keyword);
  }
  .accent-bar { position: absolute; left: 0; top: 718px; width: 14px; height: 220px; background: var(--orange); }
  .detail { position: absolute; left: 20px; display: flex; align-items: center; }
  .detail .badge {
    width: 82px; height: 82px; border-radius: 50%; flex: none;
    display: flex; align-items: center; justify-content: center;
  }
  .detail p {
    margin-left: 23px; font-family: "Cardo", serif; font-size: 23px; line-height: 29px; color: var(--white);
  }
  .detail strong { font-weight: 700; }
  .when { top: 970px; }
  .when .badge { background: var(--gold); }
  .where { top: 1085px; }
  .where .badge { background: var(--red); }
</style>
</head>
<body>
<main class="flyer">
  <div class="photo" role="img" aria-label="Photograph of a person seen from behind with arms outstretched in misty golden morning light"></div>

  <svg class="shapes" width="846" height="1200" viewBox="0 0 846 1200" aria-hidden="true">
    <rect x="430" y="0" width="416" height="11" fill="var(--orange)"/>
    <polygon points="388,11 846,11 846,522 388,66 440,11" fill="var(--navy)"/>
    <polygon points="0,0 440,0 188,370 0,182" fill="var(--teal)"/>
    <polygon points="0,72 190,262 388,66 440,0 188,370 0,182" fill="var(--teal-deep)"/>
    <line x1="375" y1="185" x2="846" y2="642" stroke="var(--line)" stroke-width="1.5"/>
    <line x1="500" y1="1088" x2="846" y2="738" stroke="var(--line)" stroke-width="1.5"/>
    <polygon points="0,938 352,938 615,1200 0,1200" fill="var(--navy)"/>
  </svg>

  <div class="brand">KORVANE</div>

  <ul class="contacts">
    <li>contact@brightmeadowfold.org
      <span class="icon"><svg width="17" height="12" viewBox="0 0 17 12"><rect x="0.8" y="0.8" width="15.4" height="10.4" fill="none" stroke="#013a5f" stroke-width="1.5"/><path d="M1 1l7.5 6L16 1" fill="none" stroke="#013a5f" stroke-width="1.5"/></svg></span></li>
    <li>www.toluvek.org
      <span class="icon"><svg width="17" height="17" viewBox="0 0 17 17" fill="none" stroke="#013a5f" stroke-width="1.3"><circle cx="8.5" cy="8.5" r="7.5"/><ellipse cx="8.5" cy="8.5" rx="3.3" ry="7.5"/><path d="M1 8.5h15M2.5 4.5h12M2.5 12.5h12"/></svg></span></li>
    <li>207 555 0183
      <span class="icon"><svg width="16" height="16" viewBox="0 0 16 16"><path d="M3 1.5l3 3-1.6 2a9 9 0 0 0 5 5l2-1.6 3 3-2 2C6 14.5 1.5 10 1 3.5z" fill="#013a5f"/></svg></span></li>
  </ul>

  <h1 class="title"><span class="cap">R</span>adiant <span class="cap">H</span>arvest<br><span class="cap">W</span>orship <span class="cap">D</span>ay</h1>
  <p class="tagline">A one day prayer retreat. Jesus Chris is Lord</p>

  <div class="accent-bar"></div>
  <p class="keywords">Prayer, Sharing the Word,<br>Panel discussion,<br>prophecy, Imapartation</p>

  <div class="detail when">
    <span class="badge"><svg width="38" height="36" viewBox="0 0 38 36"><rect x="1" y="4" width="36" height="31" rx="2" fill="#fff"/><rect x="1" y="4" width="36" height="8" fill="#e0663f"/><path d="M7 18h24M7 23h24M7 28h18" stroke="#7a8fa0" stroke-width="1.5"/><path d="M10 1v6M28 1v6" stroke="#7a8fa0" stroke-width="2"/></svg></span>
    <p>Tuesday July 2nd, 2020<br>11:00AM - 7:00PM</p>
  </div>

  <div class="detail where">
    <span class="badge"><svg width="34" height="44" viewBox="0 0 34 44"><path d="M17 1C8 1 1 8 1 17c0 11 16 26 16 26s16-15 16-26C33 8 26 1 17 1z" fill="#fff"/><circle cx="17" cy="16" r="7" fill="var(--red)"/></svg></span>
    <p>Belmora Hotel, 4876 Willowmere Street<br>Portland, Maine 04987<br><strong>(ROOM: EVERGROVE)</strong></p>
  </div>
</main>
</body>
</html>
```